Short term Rentals Marketing agency needs Web design.

We Need a web design for our new company based in Calgary, AB. We are a International Luxury home sharing company (short term rental properties, Villas, Boutique Hotels, Bed & Breakfast, Realtors, Mortgage Brokers). We would like to see designs that look simple, modern and professional. Colors would be bold (red, black, white). The final design should communicate something welcoming, symbolize innovation, and growth. Our goal is to form partnerships with Real Estate, Property Management, Short term Rental Clients to make their lives easier and increase revenue. Vlto Harbor Co. offers a flexible and secure way to market our clients properties while maintaining client satisfaction and amazing customer service. We like how https://brinkleafpromo.ca/ is interactive (when you scroll down, text gets larger). Other similar websites for Short Term Rentals is https://www.quillnestgroup.com/, https://dwelvaroo.com/, https://www.kipmarsh.com/, https://www.tarnpenny.com/about-us/, https://vantrelstays.com. We have attached our Logo.

Target Market(s)

short term rental properties, Villas, Boutique Hotels, Bed & Breakfast, Realtors, Mortgage Brokers, property owners

Industry/Entity Type

Real Estate

Coding

Coded - Design and coding required

Number of Pages Required

5+ page

Font styles to use
Sans Serif

Requirements
Must have
• Home Page, About Us page, How it works, Services, Contact us.

We like how https://brinkleafpromo.ca/ is interactive (when you scroll down, text gets larger).

We have attached our Webcopy. We would like Call to Action Buttons where they're located in the copy and page.

Must have our Logo Colors.

Other similar websites for Short Term Rentals is https://www.quillnestgroup.com/, https://dwelvaroo.com/, https://www.kipmarsh.com/, https://www.tarnpenny.com/about-us/, https://vantrelstays.com.
Nice to have
• Catchy, Interactive Home page.

Should not have
• Should not be too cluttered

```html
<!DOCTYPE html>
<html lang="en">
<head>
<meta charset="utf-8">
<title>Vlto Harbor Co. — Partner With Us</title>
<link rel="stylesheet" href="https://fonts.googleapis.com/css2?family=Poppins:wght@300;400;500;600;700&display=swap">
<style>
:root{
  --red:#e31e2d;
  --ink:#231f20;
  --dark:#2a2526;
  --slate:#1f2a36;
  --grey:#8a8a8a;
  --light:#f5f6f8;
  --white:#fff;
}
*{box-sizing:border-box;margin:0;padding:0}
html,body{width:1200px;height:4372px;overflow:hidden}
body{font-family:"Poppins",sans-serif;color:var(--ink);background:var(--white);position:relative}
.abs{position:absolute}
.center{text-align:center;left:0;width:1200px}
.label{font-size:13px;font-weight:500;color:var(--red);text-transform:uppercase;letter-spacing:.3px}
.label::before{content:"";display:inline-block;width:26px;height:2px;background:var(--red);vertical-align:middle;margin-right:6px}
.h2{font-size:40px;font-weight:500;line-height:1.15}
.lead{font-size:13px;color:var(--grey);line-height:1.85}
.btn{display:flex;align-items:center;justify-content:center;gap:8px;background:var(--red);color:var(--white);font-size:13px;font-weight:500;border-radius:3px}
.btn svg{width:11px;height:11px}

/* header + hero */
.hero{top:0;left:0;width:1200px;height:713px;background:linear-gradient(100deg,#a3add4 0%,#b3bcde 55%,#c3c9e4 100%)}
.nav{top:0;left:0;width:1200px;height:63px;border-bottom:1px solid rgba(255,255,255,.5);color:var(--white)}
.brand{top:18px;left:52px;display:flex;align-items:center;gap:8px;font-size:16px;font-weight:500;color:var(--white)}
.brand i{width:20px;height:20px;background:var(--red);display:block}
.menu{top:22px;left:395px;display:flex;gap:17px;font-size:12.5px;font-weight:500}
.phone{top:21px;left:1020px;font-size:15px;display:flex;gap:8px;align-items:center}
.divider-v{top:0;left:967px;width:1px;height:63px;background:rgba(255,255,255,.5)}
.hero-title{top:252px;left:110px;font-size:60px;font-weight:700;line-height:73px;color:var(--white);white-space:nowrap}
.hero-text{top:500px;left:112px;width:600px;font-size:12.5px;line-height:1.35;color:var(--white);font-weight:500}
.hero-btn{top:570px;left:112px;width:138px;height:44px;border:2px solid rgba(255,255,255,.6)}
.wave{left:0;top:600px;width:1200px;height:114px}

/* steps */
.step{width:300px;text-align:center}
.ring{width:118px;height:118px;border:2px solid var(--red);border-radius:50%;margin:0 auto;position:relative;display:flex;align-items:center;justify-content:center;background:var(--white)}
.ring b{position:absolute;top:-4px;right:-4px;width:30px;height:30px;border-radius:50%;background:var(--red);color:var(--white);font-size:13px;display:flex;align-items:center;justify-content:center}
.step h3{font-size:24px;font-weight:600;margin-top:24px}
.step p{font-size:13px;color:var(--grey);line-height:1.8;margin-top:8px;padding:0 22px}
.connector{top:987px;height:2px;background:var(--red)}

/* about */
.about{top:1405px;left:0;width:1200px;height:492px;background:var(--light)}

/* services */
.card{top:2094px;width:222px;height:302px;text-align:center}
.card .dot{width:78px;height:78px;border-radius:50%;margin:40px auto 0;background:#f1f1f1;display:flex;align-items:center;justify-content:center}
.card h4{font-size:17px;font-weight:500;margin-top:30px}
.card p{font-size:11.5px;color:var(--grey);line-height:1.8;margin-top:8px;padding:0 10px}
.card i{display:block;width:34px;height:2px;background:var(--red);margin:32px auto 0}
.card.active{background:var(--red);color:var(--white)}
.card.active .dot{background:var(--white)}
.card.active p{color:var(--white)}
.card.active i{background:var(--white)}

/* dark feature */
.feature{top:2522px;left:0;width:601px;height:713px;background:var(--dark);color:var(--white)}
.feat{left:35px;width:520px}
.feat .icon{width:72px;height:72px;border-radius:50%;background:var(--white);display:flex;align-items:center;justify-content:center}
.feat h3{font-size:20px;font-weight:500;margin-top:18px}
.feat p{font-size:12px;line-height:1.85;color:#c9c6c6;margin-top:8px}
.feat .more{font-size:12px;margin-top:14px;color:#d7d4d4}
.feat hr{border:0;border-top:1px solid #444;margin-top:20px}
.pager{top:3202px;left:460px;display:flex}
.pager span{width:70px;height:33px;display:flex;align-items:center;justify-content:center}

/* testimonials */
.tcard{top:3462px;width:303px;height:251px;border:2px solid #f3c3c7;border-radius:6px;padding:26px 26px 0}
.tcard .who{display:flex;gap:14px;align-items:center}
.tcard .av{width:42px;height:42px;border-radius:50%;background:linear-gradient(135deg,#3d7fb8,#9bc0dc)}
.tcard h5{font-size:20px;font-weight:400}
.tcard small{font-size:12px;color:var(--red)}
.tcard p{font-size:12px;color:#555;line-height:1.85;margin-top:24px}

/* newsletter */
.news{top:3761px;left:0;width:1200px;height:139px;background:var(--red)}
.news .field{top:44px;left:112px;width:312px;height:52px;background:var(--white);font-size:12px;color:#999;padding:17px 20px}
.news .sub{top:44px;left:424px;width:163px;height:52px;background:var(--ink);color:var(--white);font-size:12px;font-weight:500;display:flex;align-items:center;justify-content:center}
.news h3{top:50px;left:699px;font-size:33px;font-weight:500;color:var(--white)}

/* footer */
.footer{top:3900px;left:0;width:1200px;height:400px;background:var(--dark);color:#d8d5d5}
.fbrand{top:88px;left:112px;display:flex;gap:12px;align-items:center;font-size:28px;font-weight:500;color:var(--white)}
.fbrand i{width:40px;height:40px;background:var(--red);display:block}
.fcol h4{font-size:17px;font-weight:500;color:var(--red)}
.fcol .bar{width:38px;height:1px;background:#aaa;margin:20px 0 14px}
.fcol li{list-style:none;font-size:12px;line-height:21.5px}
.fcol li::before{content:"»";color:var(--red);margin-right:10px}
.social{display:flex;gap:18px}
.social span{width:12px;height:12px;border-radius:50%;background:#c9c6c6;display:block}
.copy{top:4300px;left:0;width:1200px;height:72px;background:var(--slate);color:var(--white);font-size:13px;display:flex;align-items:center;justify-content:center}
.copy em{font-style:normal;color:var(--red);margin-left:4px}
</style>
</head>
<body>

<!-- HERO -->
<section class="abs hero" role="img" aria-label="Smiling businessman in a white shirt holding out house keys beside a small model house, with a wall clock behind"></section>
<svg class="abs wave" viewBox="0 0 1200 114" preserveAspectRatio="none"><path d="M0 48 C140 20 290 40 440 78 C620 120 820 120 1000 78 C1090 58 1150 58 1200 66 L1200 114 L0 114Z" fill="#fff"/></svg>

<header class="abs nav">
  <div class="abs brand"><i></i>Vlto Harbor Co.</div>
  <nav class="abs menu"><span>Home</span><span>About Us</span><span>How it Works</span><span>Our Services ⌄</span><span>Contact Us</span></nav>
  <div class="abs divider-v"></div>
  <div class="abs phone"><svg width="13" height="13" viewBox="0 0 24 24"><path d="M6.6 10.8a15 15 0 006.6 6.6l2.2-2.2c.3-.3.7-.4 1-.2 1.1.4 2.3.6 3.6.6.6 0 1 .4 1 1V20c0 .6-.4 1-1 1A17 17 0 013 4c0-.6.4-1 1-1h3.5c.6 0 1 .4 1 1 0 1.3.2 2.5.6 3.6.1.3 0 .7-.2 1z" fill="#fff"/></svg>+(403) 555-0172</div>
</header>

<h1 class="abs hero-title">Partner With Us<br>And Let’s Start<br>Growing Together!</h1>
<p class="abs hero-text">Lorem ipsum dolor sit amet, consectetur adipisicing elit. Saepe, laborum sequi est minus autem accusantium, voluptatem. Pariatur assumenda, veritatis eligendi?</p>
<a class="abs btn hero-btn">Let’s Start <svg viewBox="0 0 12 12"><path d="M1 6h9M6 2l4 4-4 4" stroke="#fff" stroke-width="1.6" fill="none"/></svg></a>

<!-- STEPS -->
<div class="abs center label" style="top:766px">Lorem Ipsum Dolor</div>
<h2 class="abs center h2" style="top:792px">Lorem Ipsum Dolor Sit Amet.</h2>
<p class="abs center lead" style="top:848px">Lorem ipsum dolor sit amet, consectetur adipisicing elit. Nemo mollitia eius voluptate!<br>Distinctio earum aliquam fugit veritatis, illo saepe harum.</p>

<div class="abs connector" style="left:324px;width:216px"></div>
<div class="abs connector" style="left:658px;width:216px"></div>

<div class="abs step" style="top:929px;left:115px">
  <div class="ring"><b>1</b><svg width="54" height="54" viewBox="0 0 54 54" fill="none" stroke="#e31e2d" stroke-width="2"><path d="M8 26L27 10l19 16M13 22v22h28V22"/><rect x="22" y="31" width="10" height="13"/></svg></div>
  <h3>Title Here</h3>
  <p>Lorem ipsum dolor sit amet, consectetur adipisicing elit. Rorum culpa quas aperiam nulla nesciunt aspernatur a doloremque necessitatibus natus non.</p>
</div>
<div class="abs step" style="top:929px;left:449px">
  <div class="ring"><b>2</b><svg width="54" height="54" viewBox="0 0 54 54" fill="none" stroke="#e31e2d" stroke-width="2"><rect x="12" y="8" width="30" height="38" rx="2"/><path d="M18 18h18M18 26h18M18 34h10"/></svg></div>
  <h3>Title Here</h3>
  <p>Lorem ipsum dolor sit amet, consectetur adipisicing elit. Magnam consectetur laboriosam veritatis possimus illo officiis quisquam! Iusto ex, repellendus accusantium.</p>
</div>
<div class="abs step" style="top:929px;left:782px">
  <div class="ring"><b>3</b><svg width="54" height="54" viewBox="0 0 54 54" fill="none" stroke="#e31e2d" stroke-width="2"><path d="M10 42l14-14M24 28l6 6M30 34l14-14M14 14l8 8M40 12v10h-10"/></svg></div>
  <h3>Title Here</h3>
  <p>Lorem ipsum dolor sit amet, consectetur adipisicing elit. Magnam consectetur laboriosam veritatis possimus illo officiis quisquam! Iusto ex, repellendus accusantium.</p>
</div>
<a class="abs btn" style="top:1269px;left:507px;width:184px;height:46px">See How It Works <svg viewBox="0 0 12 12"><path d="M1 6h9M6 2l4 4-4 4" stroke="#fff" stroke-width="1.6" fill="none"/></svg></a>

<!-- ABOUT -->
<section class="abs about">
  <div class="abs" style="top:0;left:112px;width:474px;height:492px;background:linear-gradient(135deg,#3b3f43 0%,#8d8a84 45%,#d9d6cf 75%,#6c6a66 100%)" role="img" aria-label="Woman writing in a spiral notebook at a desk beside a laptop"></div>
  <div class="abs label" style="top:63px;left:675px">About Vlto Harbor</div>
  <h2 class="abs h2" style="top:95px;left:675px;width:440px;font-size:37px">Lorem Ipsum Dolor Sit Amet.</h2>
  <p class="abs lead" style="top:197px;left:675px;width:420px;font-size:12.5px;line-height:1.9">Vlto Harbor Co. is here to manage and market your short-term rental properties so you don’t have to. Enjoy peace of mind in knowing your short-term rental properties, vacation homes, villas, hotels, and B&amp;Bs are safe, secure, and profitable - no matter where you are in the world. We will help you market, manage, and capitalize on everything, from your newest bookings to house cleaning and upkeep.</p>
  <a class="abs btn" style="top:401px;left:675px;width:119px;height:32px">Read More</a>
</section>

<!-- SERVICES -->
<div class="abs center label" style="top:1930px">Lorem Ipsum</div>
<h2 class="abs center h2" style="top:1956px">Powerful Better Together</h2>
<p class="abs center lead" style="top:2012px">Lorem ipsum dolor sit amet, consectetur adipisicing elit. Error sequi saepe, quod unde<br>repellendus aperiam.</p>

<div class="abs card" style="left:113px"><div class="dot"><svg width="34" height="34" viewBox="0 0 54 54" fill="none" stroke="#e31e2d" stroke-width="2.4"><path d="M8 26L27 10l19 16M13 22v22h28V22"/></svg></div><h4>Title Here</h4><p>Lorem ipsum dolor sit amet consectetur adipisicing elit, sed do eiusmod</p><i></i></div>
<div class="abs card active" style="left:363px"><div class="dot"><svg width="34" height="34" viewBox="0 0 54 54" fill="none" stroke="#e31e2d" stroke-width="2.4"><path d="M10 42l14-14M24 28l6 6M30 34l14-14M14 14l8 8"/></svg></div><h4>Title Here</h4><p>Lorem ipsum dolor sit amet consectetur adipisicing elit, sed do eiusmod</p><i></i></div>
<div class="abs card" style="left:614px"><div class="dot"><svg width="34" height="34" viewBox="0 0 54 54" fill="none" stroke="#e31e2d" stroke-width="2.4"><rect x="12" y="8" width="30" height="38" rx="2"/><path d="M18 18h18M18 26h18"/></svg></div><h4>Title Here</h4><p>Lorem ipsum dolor sit amet consectetur adipisicing elit, sed do eiusmod</p><i></i></div>
<div class="abs card" style="left:865px"><div class="dot"><svg width="34" height="34" viewBox="0 0 54 54" fill="none" stroke="#e31e2d" stroke-width="2.4"><path d="M10 44V20l17-10 17 10v24zM20 44V30h14v14"/></svg></div><h4>Title Here</h4><p>Lorem ipsum dolor sit amet consectetur adipisicing elit, sed do eiusmod</p><i></i></div>

<a class="abs btn" style="top:2452px;left:507px;width:123px;height:44px">View All <svg viewBox="0 0 12 12"><path d="M1 6h9M6 2l4 4-4 4" stroke="#fff" stroke-width="1.6" fill="none"/></svg></a>

<!-- FEATURE -->
<section class="abs feature">
  <div class="abs feat" style="top:33px">
    <div class="icon"><svg width="36" height="36" viewBox="0 0 54 54" fill="none" stroke="#e31e2d" stroke-width="2.4"><path d="M10 42l14-14M24 28l6 6M30 34l14-14M14 14l8 8"/></svg></div>
    <h3>Increase Your Revenue (Without The Hassle)</h3>
    <p>Having Vlto Harbor Co. manage and market your rental property lets you benefit from increased revenues without having to put in the hours of work yourself. Vlto Harbor Co. will manage your property listings, advertise your listings, optimize your rental pricing, increase your occupancy, and help you offer the very best customer experience.</p>
    <div class="more">READ MORE ›</div>
    <hr>
  </div>
  <div class="abs feat" style="top:349px">
    <div class="icon"><svg width="36" height="36" viewBox="0 0 54 54" fill="none" stroke="#e31e2d" stroke-width="2.4"><path d="M8 26L27 10l19 16M13 22v22h28V22"/></svg></div>
    <h3>Receive Constant Support</h3>
    <p>Our dedicated team is there to take care of your property so that you don’t have to. Our affordable and professional services include being there to support your guests, constant technical communication, and on-site operations management.</p>
    <p style="margin-top:14px">Lorem ipsum dolor sit amet, consectetur adipisicing elit. Sunt tempore, odio blanditiis dolorum tenetur qui provident assumenda eos corporis magni.</p>
    <div class="more">READ MORE ›</div>
    <hr>
  </div>
</section>
<div class="abs" style="top:2522px;left:602px;width:598px;height:713px;background:linear-gradient(150deg,#6f4a2c 0%,#2f4f8e 40%,#26457f 60%,#c9c3b6 100%)" role="img" aria-label="Man in a blue shirt using a smartphone at a desk with papers and a pen"></div>
<div class="abs pager">
  <span style="background:#555"><svg width="12" height="8" viewBox="0 0 12 8"><path d="M1 7l5-5 5 5" stroke="#fff" stroke-width="1.8" fill="none"/></svg></span>
  <span style="background:var(--red)"><svg width="12" height="8" viewBox="0 0 12 8"><path d="M1 1l5 5 5-5" stroke="#fff" stroke-width="1.8" fill="none"/></svg></span>
</div>

<!-- TESTIMONIALS -->
<div class="abs center label" style="top:3289px">Testimonial</div>
<h2 class="abs center h2" style="top:3315px">"What Is Our Client Says"</h2>
<p class="abs center lead" style="top:3371px">Lorem ipsum dolor sit amet, consectetur adipisicing elit. Est dolorem ex commodi dolorum<br>ipsa nobis.</p>

<div class="abs tcard" style="left:120px"><div class="who"><div class="av" role="img" aria-label="Client portrait"></div><div><h5>John Doe</h5><small>CFO At Qarvel</small></div></div><p>Lorem ipsum dolor sit amet, consectetur adipisicing elit. Sit nostrum, provident commodi fuga. Alias accusantium deserunt, similique vitae possimus, fugiat omnis reiciendis iusto consequatur quibusdam!</p></div>
<div class="abs tcard" style="left:450px"><div class="who"><div class="av" role="img" aria-label="Client portrait"></div><div><h5>John Doe</h5><small>CEO</small></div></div><p>Lorem ipsum dolor sit amet, consectetur adipisicing elit. Sit nostrum, provident commodi fuga. Alias accusantium deserunt, similique vitae possimus, fugiat omnis reiciendis iusto consequatur quibusdam!</p></div>
<div class="abs tcard" style="left:779px"><div class="who"><div class="av" role="img" aria-label="Client portrait"></div><div><h5>John Doe</h5><small>HR Manager</small></div></div><p>Lorem ipsum dolor sit amet, consectetur adipisicing elit. Sit nostrum, provident commodi fuga. Alias accusantium deserunt, similique vitae possimus, fugiat omnis reiciendis iusto consequatur quibusdam!</p></div>

<!-- NEWSLETTER -->
<section class="abs news">
  <div class="abs field">Your Email</div>
  <div class="abs sub">SUBSCRIBE NOW</div>
  <h3 class="abs">Subscribe Our Newsletter</h3>
</section>

<!-- FOOTER -->
<footer class="abs footer">
  <div class="abs fbrand"><i></i>Vlto Harbor Co.</div>
  <p class="abs" style="top:182px;left:112px;width:270px;font-size:13px;line-height:1.85">Lorem ipsum dolor sit amet consectetur adipi sicing elit, sed do eiusmod tempor incididunt ut labore et dolore magna aliqua dolor.</p>
  <div class="abs" style="top:300px;left:112px;font-size:15px;font-weight:600;color:#fff;display:flex;gap:16px;align-items:center"><svg width="15" height="15" viewBox="0 0 24 24"><path d="M6.6 10.8a15 15 0 006.6 6.6l2.2-2.2c.3-.3.7-.4 1-.2 1.1.4 2.3.6 3.6.6.6 0 1 .4 1 1V20c0 .6-.4 1-1 1A17 17 0 013 4c0-.6.4-1 1-1h3.5c.6 0 1 .4 1 1 0 1.3.2 2.5.6 3.6.1.3 0 .7-.2 1z" fill="#e31e2d"/></svg>+403 555 0172</div>
  <div class="abs" style="top:333px;left:112px;font-size:15px;font-weight:600;color:#fff;display:flex;gap:16px;align-items:center"><svg width="15" height="12" viewBox="0 0 24 18"><rect width="24" height="18" rx="2" fill="#e31e2d"/><path d="M1 2l11 8 11-8" stroke="#2a2526" stroke-width="2" fill="none"/></svg>hello@vltoharbor.co</div>

  <div class="abs fcol" style="top:96px;left:447px"><h4>Quick Links</h4><div class="bar"></div><ul><li>About Us</li><li>Our Services</li><li>How It Works</li><li>Contact Us</li></ul></div>
  <div class="abs fcol" style="top:96px;left:699px"><h4>Our Services</h4><div class="bar"></div><ul><li>Service 1</li><li>Service 2</li><li>Service 3</li><li>Service 4</li><li>Service 5</li><li>Service 6</li></ul></div>

  <div class="abs" style="top:87px;left:963px;width:116px;height:40px;background:var(--red);color:#fff;font-size:15px;display:flex;align-items:center;justify-content:center;border-radius:2px">Book Now</div>
  <div class="abs" style="top:143px;left:975px;width:92px;height:40px;border:1px solid #bbb;color:#fff;font-size:15px;display:flex;align-items:center;justify-content:center;border-radius:2px">Join Us</div>
  <div class="abs social" style="top:252px;left:963px"><span></span><span></span><span></span><span></span></div>
</footer>
<div class="abs copy">© 2020 All Rights Reserved by<em>Vlto Harbor</em></div>

</body>
</html>
```